Career development coaching - school lever to adults, needs a business card

Tandem Lark - An independent Career Advice business that provides 1-2-1 advice,for career development, entrepreneurial support and workshops needs a business card. Our clients of all ages (school leaver to adults looking for a career move) and universities and colleges. We would like the card to be double-sided with a modern, professional look. Looking for something professional yet very creative and original. Want a standard size business card that inspires a second look because it stands out from the rest.

One side of the card to have a design incorporating the logo with Tandem Lark name with the strap line “Guiding you toward tomorrow” and space for the company website

Other side of the card to the logo/Tandem Lark name and the usual contact information:
Individual Name
Job Title (for example, Director)
Phone number
Email address
Company website address

Facebook, LinkedIn and Twitter links will need to go somewhere (back or front!)

The design will be used for 3 individuals so should be editable so that we can update as needed/as we grow.

Attached is the company logo/colours to be incorporated.

Target Market(s)

1-2-1 advice,for career development, entrepreneurial support and workshops needs a business card. Our clients of all ages (school leaver to adults looking for a career move) and universities and colleges.

Industry/Entity Type

Consulting

Contact Information for Business Card

Individual Name
Phone number
Email address
Company website address

Font styles to use
Sans Serif

Colors
0255a3
3176b5
faa54b
f78f20
85acd3
cfdeed

Requirements
Must have
• use the Tandem Lark Logo in some way - using the colours and the blue/orange palette
• For the logo - hope this makes sense to someone or if they direclty relate to the logo image attached!
• For the Orange:- Pantone 1585 C
• In CMYK : C3 M71 Y100 K0
• For the Blue:- 100% Pantone 7469 C
• In CMYK : C100 M62 Y27 K7
• Please feel free to contact me with any questions for more info
Nice to have
• happy to see any creative designs
Should not have
• Nothing too traditional,

```html
<!DOCTYPE html>
<html lang="en">
<head>
<meta charset="utf-8">
<title>Tandem Lark – Business Card</title>
<link rel="stylesheet" href="https://fonts.googleapis.com/css2?family=Open+Sans:wght@400;600;700&display=swap">
<style>
  :root {
    --brand-blue: #11658f;
    --brand-orange: #ee7431;
    --card-white: #ffffff;
    --stage: #e9ecef;
    --card-shadow: rgba(20, 40, 60, 0.18);
  }
  * { box-sizing: border-box; margin: 0; padding: 0; }
  html, body {
    width: 1200px; height: 900px; overflow: hidden;
    background: var(--stage);
    font-family: "Open Sans", Arial, sans-serif;
  }
  .canvas { position: relative; width: 1200px; height: 900px; }

  .card {
    position: absolute;
    background: var(--card-white);
    box-shadow: 0 6px 18px var(--card-shadow);
    overflow: hidden;
  }

  /* Contact side */
  .card--contact { left: 237px; top: 62px; width: 556px; height: 343px; }
  .wordmark {
    font-family: "Open Sans", Arial, sans-serif;
    font-weight: 600;
    font-variant: small-caps;
    letter-spacing: 1.5px;
    color: var(--brand-blue);
    white-space: nowrap;
  }
  .card--contact .wordmark {
    position: absolute; left: 37px; top: 24px; font-size: 36px; line-height: 1;
  }
  .person { position: absolute; left: 38px; top: 89px; }
  .person__name { font-size: 18px; font-weight: 600; color: var(--brand-blue); line-height: 1.2; }
  .person__surname { color: var(--brand-orange); }
  .person__role { font-size: 14px; color: var(--brand-orange); line-height: 1.3; }

  .contact-band {
    position: absolute; left: 0; top: 148px; width: 400px; height: 163px;
    background: var(--brand-blue);
    color: var(--card-white);
    padding: 10px 0 0 36px;
    font-size: 14.5px;
  }
  .contact-list { list-style: none; }
  .contact-list li { display: flex; align-items: center; height: 20px; }
  .contact-list--social { margin-top: 13px; }
  .contact-list svg { width: 12px; height: 12px; margin-right: 11px; flex: none; }
  .social-dot { width: 12px; height: 12px; border-radius: 50%; background: var(--card-white); margin-right: 11px; flex: none; }

  .brand-seal__circle {
    position: absolute;
    border-radius: 50%;
    background: var(--brand-orange);
  }
  .card--contact .brand-seal__circle {
    left: 336px; top: 146px; width: 168px; height: 168px;
    border: 6px solid var(--card-white);
  }

  /* Brand side */
  .card--brand { left: 457px; top: 518px; width: 560px; height: 344px; text-align: center; }
  .card--brand .brand-seal__circle {
    left: 221px; top: 52px; width: 124px; height: 124px;
  }
  .card--brand .wordmark {
    position: absolute; left: 0; right: 0; top: 194px; font-size: 35px; line-height: 1;
  }
  .strapline {
    position: absolute; left: 0; right: 0; top: 252px;
    font-size: 19px; font-weight: 600; color: var(--brand-orange);
    text-transform: uppercase; letter-spacing: 0.2px;
  }
</style>
</head>
<body>
<main class="canvas">

  <section class="card card--contact" aria-label="Business card, contact side">
    <div class="wordmark">Tandem Lark</div>
    <div class="person">
      <div class="person__name">Daniel <span class="person__surname">Hartley</span></div>
      <div class="person__role">Managing Director</div>
    </div>

    <div class="contact-band">
      <ul class="contact-list">
        <li>
          <svg viewBox="0 0 12 12" aria-hidden="true"><path fill="#fff" d="M2.3 0.6l2 2.1-1 1.3c.7 1.6 1.9 2.8 3.5 3.5l1.3-1 2.1 2-1.1 2.3C4.9 10.6 1.4 7.1 0.6 2.9z"/></svg>
          044-987 650 321
        </li>
        <li>
          <svg viewBox="0 0 12 12" aria-hidden="true"><rect x="1" y="2.5" width="10" height="7" fill="#fff"/><path d="M1 2.8l5 3.6 5-3.6" fill="none" stroke="#11658f" stroke-width="1"/></svg>
          hello@tandemlark.com
        </li>
        <li>
          <svg viewBox="0 0 12 12" aria-hidden="true"><circle cx="6" cy="6" r="5" fill="#fff"/><path d="M1 6h10M6 1c-2 2.6-2 7.4 0 10M6 1c2 2.6 2 7.4 0 10" fill="none" stroke="#11658f" stroke-width="0.8"/></svg>
          www.tandemlark.com
        </li>
      </ul>
      <ul class="contact-list contact-list--social">
        <li><span class="social-dot"></span>tandemlark.com/connect</li>
        <li><span class="social-dot"></span>tandemlark.com/network</li>
        <li><span class="social-dot"></span>tandemlark.com/updates</li>
      </ul>
    </div>

    <div class="brand-seal__circle"></div>
  </section>

  <section class="card card--brand" aria-label="Business card, brand side">
    <div class="brand-seal__circle"></div>
    <div class="wordmark">Tandem Lark</div>
    <p class="strapline">Guiding you toward tomorrow</p>
  </section>

</main>
</body>
</html>
```